tax advisory service business cards
Professional
Loretta Fenwick
Tax Advisory Specialist
51924 HOLLISTER LANE SUITE C
PRAIRIEVILL, LA 70812
FISCAL9COUNSELDESK@QUILLMAIL.COM
FCD4FILE.COM

```html
<!DOCTYPE html>
<html lang="en">
<head>
<meta charset="utf-8">
<title>Ledgerwise Counsel – Business Cards</title>
<link href="https://fonts.googleapis.com/css2?family=Arimo:wght@400;700&display=swap" rel="stylesheet">
<style>
  :root {
    --bg: #e6e4e1;
    --card: #ffffff;
    --navy: #1f3e78;
    --ink: #1b1b1b;
    --grey: #6e6e6e;
    --gold: #c9a227;
    --gold-light: #e9c95a;
    --black: #111111;
    --pale-gold: #f3e6b8;
  }
  * { margin: 0; padding: 0; box-sizing: border-box; }
  html, body { width: 1200px; height: 754px; overflow: hidden; }
  body {
    background: var(--bg);
    font-family: "Arimo", Arial, sans-serif;
    position: relative;
  }
  .card {
    position: absolute;
    top: 217px;
    width: 540px;
    height: 320px;
    background: var(--card);
    border-radius: 22px;
    overflow: hidden;
    box-shadow: 0 8px 22px rgba(0,0,0,0.18);
  }
  .card--front { left: 40px; }
  .card--back { left: 620px; }

  .card__wave { position: absolute; left: 0; top: 0; width: 540px; height: 320px; }

  .brand {
    position: absolute;
    left: 22px;
    top: 70px;
    width: 170px;
    text-align: center;
  }
  .brand__mark {
    width: 54px; height: 54px;
    border-radius: 50%;
    background: var(--navy);
    border: 3px solid var(--gold);
    margin: 0 auto 12px;
  }
  .brand__name {
    font-size: 12px;
    font-weight: 700;
    color: var(--ink);
    letter-spacing: 0.2px;
    text-transform: uppercase;
  }

  .person {
    position: absolute;
    left: 210px;
    top: 34px;
  }
  .person__name { font-size: 23px; font-weight: 700; color: var(--navy); }
  .person__title { font-size: 10px; color: var(--grey); margin-top: 2px; }

  .address {
    position: absolute;
    left: 210px;
    top: 110px;
    font-size: 10px;
    color: var(--grey);
    line-height: 1.45;
  }
  .contacts {
    position: absolute;
    left: 210px;
    top: 156px;
    list-style: none;
    font-size: 10px;
    color: var(--grey);
    line-height: 1.5;
  }
  .contacts li { display: flex; align-items: center; gap: 6px; }
  .contacts .icon { width: 9px; height: 9px; flex: none; }

  .back__seal {
    position: absolute;
    left: -40px;
    top: 150px;
    width: 240px;
    height: 240px;
    border-radius: 50%;
    background: radial-gradient(circle, var(--navy) 0 52%, var(--pale-gold) 53% 70%, var(--gold) 71% 100%);
  }
  .back__brand {
    position: absolute;
    right: 26px;
    bottom: 58px;
    font-size: 14px;
    font-weight: 700;
    color: var(--ink);
    text-transform: uppercase;
  }
</style>
</head>
<body>

<section class="card card--front" aria-label="Business card front">
  <svg class="card__wave" viewBox="0 0 540 320" aria-hidden="true">
    <defs>
      <linearGradient id="goldBand" x1="0" y1="0" x2="1" y2="0">
        <stop offset="0" stop-color="#e9c95a"/>
        <stop offset="0.5" stop-color="#c9a227"/>
        <stop offset="1" stop-color="#a9841a"/>
      </linearGradient>
    </defs>
    <path d="M0,252 C160,298 330,228 540,186 L540,320 L0,320 Z" fill="url(#goldBand)"/>
    <path d="M0,246 C160,292 330,222 540,178 L540,206 C330,246 170,306 0,262 Z" fill="#111111"/>
    <path d="M0,298 C190,326 370,262 540,248 L540,320 L0,320 Z" fill="#ffffff"/>
  </svg>

  <div class="brand">
    <div class="brand__mark"></div>
    <div class="brand__name">Ledgerwise Counsel, Inc.</div>
  </div>

  <div class="person">
    <div class="person__name">Loretta Fenwick</div>
    <div class="person__title">Tax Advisory Specialist</div>
  </div>

  <address class="address" style="font-style:normal">
    51924 HOLLISTER LANE SUITE C<br>
    Prairieville, LA 70812
  </address>

  <ul class="contacts">
    <li><svg class="icon" viewBox="0 0 10 10"><rect width="10" height="10" rx="1.5" fill="#c9a227"/></svg>225-555-0148</li>
    <li><svg class="icon" viewBox="0 0 10 10"><rect width="10" height="10" rx="1.5" fill="#c9a227"/></svg>FISCAL9COUNSELDESK@QUILLMAIL.COM</li>
    <li><svg class="icon" viewBox="0 0 10 10"><rect width="10" height="10" rx="1.5" fill="#c9a227"/></svg>WWW.FCD4FILE.COM</li>
  </ul>
</section>

<section class="card card--back" aria-label="Business card back">
  <div class="back__seal" role="img" aria-label="Large brand seal decoration in navy and gold"></div>
  <div class="back__brand">Ledgerwise Counsel, Inc.</div>
</section>

</body>
</html>
```